Web Design Project (Mente Lumo)

We are going to do a therapy template to a psychologist. The site already exists, adress: www.mentelumo.net. So, its a total redesign job. I'm from Brazil, the language is PT-BR, so I'm gonna translate what you think be necessary. You can use the current structure from the website as a base to the new design. Check this template to see what I usually like: http://www.layoutkiosk.example/demo/51937.html
Updates

I'm waiting for new creative designs. The 'structure' image is just for 'pb'.

Requirements
Must have
• We need a modern menu, it should use a cool font style and make some kind of effect and little noise when the user pass over with the mouse (FLASH/HTML 5). The main page must emphasize the fact that we offer online treatment, like a picture or frame saying "Online Treatment, click here". It must also show the therapist picture and her name. The colors need to pass a tranquility feeling. The clinic telephone must always be present, doesn't matter which page the user is. The website must adapt to any resolution above 1024x768, crossbrowsing and accept javascript (I'll use www.agendrix.example, so its necessary embed code)
Nice to have
• I would appreciate if there was some kind of slow background animation, passing behind the text using the transparency.
Should not have
• Can't take too long to load, and won't have news or blog

```html
<!DOCTYPE html>
<html lang="pt-BR">
<head>
<meta charset="utf-8">
<title>Mente Lumo — Terapia Cognitiva</title>
<link href="https://fonts.googleapis.com/css2?family=Nunito+Sans:ital,wght@0,400;0,600;0,700;0,800;1,400;1,700;1,800&display=swap" rel="stylesheet">
<style>
:root{
  --topbar:#2d6d8f;
  --nav:#5fb2cc;
  --nav-dark:#3d93b3;
  --hero:#e6f3f7;
  --ink:#2b2b2b;
  --ink-soft:#3a3a3a;
  --blue-title:#2f6e96;
  --accent-yellow:#e8eaa8;
  --button:#7ac5dc;
  --cream:#f4f7ea;
  --footer:#5fb3cb;
  --footer-dark:#4ea3bd;
  --white:#ffffff;
  --pink:#a85a85;
  --steel:#5b8db0;
  --green:#7cb05e;
}
*{margin:0;padding:0;box-sizing:border-box}
html,body{width:1200px;height:1111px;overflow:hidden}
body{font-family:"Nunito Sans",sans-serif;color:var(--ink);background:var(--hero);position:relative}
.abs{position:absolute}
.topbar{left:0;top:0;width:1200px;height:37px;background:var(--topbar);color:var(--white);font-weight:700;font-size:12.5px}
.topbar .address{position:absolute;left:150px;top:10px}
.topbar .phones{position:absolute;right:150px;top:10px;word-spacing:2px}
.topbar .phones span{margin-left:16px}
.navbar{left:0;top:37px;width:1200px;height:53px;background:linear-gradient(var(--nav),var(--nav-dark));box-shadow:0 3px 6px rgba(0,0,0,.12)}
.nav-item{position:absolute;top:19px;color:var(--white);font-weight:700;font-size:13.5px;text-shadow:0 1px 1px rgba(0,0,0,.3)}
.nav-item.active{color:var(--accent-yellow)}
.nav-item.active::before{content:"";position:absolute;left:-25px;right:-25px;top:-20px;height:3px;background:var(--accent-yellow)}
.dot{position:absolute;top:25px;width:5px;height:5px;border-radius:50%;background:#dff2f8}
.logo-plate{left:470px;top:6px;width:242px;height:110px;background:linear-gradient(#f4fbfd,#d5eef6);border:3px solid #9fd6e6;border-radius:40px 40px 60px 60px;display:flex;align-items:center;justify-content:center;gap:10px;box-shadow:0 2px 6px rgba(0,0,0,.15)}
.logo-plate .mark{width:16px;height:16px;border-radius:50%;background:var(--nav-dark)}
.logo-plate .name{font-weight:700;font-size:24px;color:var(--blue-title)}
.hero-intro{left:218px;top:208px;font-style:italic;font-size:26px;color:var(--blue-title)}
.hero-title{left:298px;top:242px;font-style:italic;font-weight:800;font-size:29px;color:#1f1f1f}
.hero-text{left:220px;top:302px;width:370px;font-size:12.4px;line-height:22.5px;color:var(--ink-soft)}
.read-more{left:333px;top:471px;width:239px;height:44px;border-radius:22px;background:var(--button);border:1px solid #5aaec7;color:var(--white);font-size:16px;font-weight:600;display:flex;align-items:center;justify-content:center;text-shadow:0 1px 1px rgba(0,0,0,.3);box-shadow:0 4px 6px rgba(0,0,0,.15)}
.head-art{left:660px;top:170px;width:400px;height:437px;background:
  radial-gradient(ellipse 46% 42% at 45% 42%,rgba(110,185,215,.55),rgba(110,185,215,0) 100%),
  radial-gradient(ellipse 55% 60% at 50% 50%,#ffffff 0%,rgba(255,255,255,.85) 55%,rgba(230,243,247,0) 100%)}
.content{left:0;top:607px;width:1200px;height:337px;background:var(--cream);border-top:1px solid #d9e3d4}
.photo{background:linear-gradient(#bdbdbd,#6e6e6e);border:3px solid var(--white);outline:1px solid #bbb;box-shadow:0 4px 6px rgba(0,0,0,.2)}
.profile-photo{left:162px;top:634px;width:137px;height:167px}
.office-photo{left:483px;top:634px;width:261px;height:214px;background:linear-gradient(135deg,#c7d8c8,#8a9a7a 60%,#4b4b42)}
.role{left:162px;top:808px;width:142px;text-align:center;font-size:12.5px;color:var(--blue-title)}
.therapist{left:162px;top:823px;width:142px;text-align:center;font-size:14px;font-weight:700;color:#111}
.crp{left:162px;top:843px;width:142px;text-align:center;font-size:10.5px;color:#555}
.section-title{font-style:italic;font-weight:400;font-size:18px;color:var(--blue-title);padding:0 2px 3px;border-bottom:2px solid var(--blue-title)}
.section-text{font-size:12.5px;line-height:22.5px;color:var(--ink-soft)}
.cta{top:874px;height:53px;border:1px solid #c9ccc0;background:var(--white)}
.cta .bar{position:absolute;left:10px;right:10px;top:10px;height:33px;color:var(--white);font-size:14px;display:flex;align-items:center;text-shadow:0 1px 1px rgba(0,0,0,.3)}
.cta-icon{position:absolute;border-radius:8px}
.footer{left:0;top:944px;width:1200px;height:167px;background:linear-gradient(var(--footer),var(--footer-dark))}
.reviews-label{left:230px;top:970px;font-size:13.5px;line-height:21px;color:var(--accent-yellow);letter-spacing:.5px}
.review-quote{left:409px;top:970px;font-style:italic;font-size:12.5px;line-height:20px;color:var(--white)}
.rule{left:166px;width:873px;height:1px;background:rgba(255,255,255,.45)}
.footer-address{left:0;top:1046px;width:1200px;text-align:center;font-style:italic;font-size:12.5px;color:var(--white)}
.footer-address b{color:var(--accent-yellow)}
.copyright{left:0;top:1088px;width:1200px;text-align:center;font-size:10px;color:var(--white)}
</style>
</head>
<body>
<header>
  <div class="abs topbar">
    <div class="address">Rua das Acácias, 142, Sala 58 - Centro - Vila Serena</div>
    <div class="phones"><span>(11) 4020-1735</span><span>(11) 9180-4426</span><span>(11) 7655-3108</span></div>
  </div>
  <nav class="abs navbar">
    <span class="nav-item" style="left:152px">HOME</span>
    <span class="dot" style="left:217px"></span>
    <span class="nav-item active" style="left:251px">SERVIÇOS</span>
    <span class="dot" style="left:335px"></span>
    <span class="nav-item" style="left:370px">INDICAÇÕES</span>
    <span class="nav-item" style="left:735px">PERGUNTAS</span>
    <span class="dot" style="left:824px"></span>
    <span class="nav-item" style="left:850px">LOCALIZAÇÃO</span>
    <span class="dot" style="left:953px"></span>
    <span class="nav-item" style="left:978px">CONTATO</span>
  </nav>
  <div class="abs logo-plate"><span class="mark"></span><span class="name">Mente Lumo</span></div>
</header>

<section class="hero">
  <div class="abs hero-intro">O que é a</div>
  <h1 class="abs hero-title">Terapia Cognitiva?</h1>
  <p class="abs hero-text">A Terapia Cognitiva tem como método a interpretação de processos e conteúdos mentais (as cognições), e sua influência na vida cotidiana. O comportamento e a emoção vêm depois do processamento cognitivo. É vital conhecermos nossos pensamentos para termos controle sobre eles, e assim podemos: nutri-los, expandi-los, reduzi-los ou rejeitá-los.</p>
  <div class="abs read-more">Leia Mais</div>
  <div class="abs head-art" role="img" aria-label="Ilustração de uma cabeça em perfil com engrenagens azuis no lugar do cérebro"></div>
</section>

<section class="abs content"></section>
<div class="abs photo profile-photo" role="img" aria-label="Foto da psicóloga"></div>
<div class="abs role">Psicóloga</div>
<div class="abs therapist">Lívia Moraes</div>
<div class="abs crp">CRP: 6/204518</div>
<h2 class="abs section-title" style="left:318px;top:634px">Perfil</h2>
<p class="abs section-text" style="left:318px;top:667px;width:145px">Formada em Psicologia pela Universidade Vale Claro, com especialização pelo IEC (Instituto de Estudos Cognitivos).</p>
<div class="abs photo office-photo" role="img" aria-label="Foto do consultório com poltronas, planta e armário"></div>
<h2 class="abs section-title" style="left:762px;top:634px">Quem somos?</h2>
<p class="abs section-text" style="left:762px;top:667px;width:275px">A Mente Lumo realiza orientação psicológica online e terapias presenciais, seguindo as normas e diretivas do Conselhos Nacional da Psicologia, objetivando prestar um serviço de qualidade e propiciando um atendimento centrado no cliente, seguindo os padrões éticos e legais.</p>

<div class="abs cta" style="left:162px;width:277px">
  <div class="bar" style="background:linear-gradient(90deg,#c58aa8,var(--pink));left:40px;padding-left:22px"><span><i>Agende online</i> seu atendimento</span></div>
  <div class="cta-icon" style="left:0;top:-4px;width:62px;height:56px;background:linear-gradient(#9fc4dc,#3c5d8a)" role="img" aria-label="Ilustração de atendente com fone"></div>
</div>
<div class="abs cta" style="left:465px;width:276px">
  <div class="bar" style="background:linear-gradient(90deg,#86aac3,var(--steel));justify-content:center;font-size:21px;padding-left:40px"><span><b style="color:var(--accent-yellow)">(11)</b> 4020-1735</span></div>
  <svg class="cta-icon" style="left:38px;top:-4px" width="34" height="62" viewBox="0 0 34 62"><rect x="2" y="1" width="30" height="60" rx="5" fill="#222"/><rect x="5" y="8" width="24" height="44" fill="#3aa0e0"/></svg>
</div>
<div class="abs cta" style="left:765px;width:276px">
  <div class="bar" style="background:linear-gradient(90deg,#95c47a,var(--green));justify-content:center;padding-left:55px"><span>Veja onde <b>estamos</b></span></div>
  <div class="cta-icon" style="left:24px;top:-4px;width:58px;height:56px;background:linear-gradient(135deg,#e7e7e7,#4d8ac0)" role="img" aria-label="Ilustração de mapa com bússola"></div>
</div>

<footer class="abs footer"></footer>
<div class="abs reviews-label">AVALIAÇÕES DE<br>CLIENTES SATISFEITOS:</div>
<blockquote class="abs review-quote">"I just want to thank you for the fastest shipment and best service I could have ever gotten.<br>When I placed my order with you I was a first time customer but I will not be a last time one."</blockquote>
<div class="abs rule" style="top:1029px"></div>
<div class="abs footer-address">Rua das Acácias, 142, 5º andar, Sala 58 - Centro - Vila Serena, SP - <b>Clique aqui ver o mapa</b> - contato@mentelumo.net</div>
<div class="abs rule" style="top:1078px"></div>
<div class="abs copyright">Copyright © 2012 - Todoa os diretos reservados</div>
</body>
</html>
```